Direct Mail Marketing Postcard Template Design

Mine is a residential real estate marketing service for "Fixer Upper" properties in Central Indiana. My company owns the properties being promoted on a proprietary/branded web site (also being developed by Corvel Press) and by Direct Mail . The properties for sale are not traditional real estate "listings".

I expect the post card and the web site to establish and promote the "new" brand for Bramble Arc Holdings, Inc.

The post card will be mailed to specific niche markets; primarily "Hands On" real estate investors, Rehabbers, Landlords, and First Time Home Buyers. The cards will routinely be mailed to investors and to residents in the area surrounding a property for sale to generate home buyer phone call inquiry, word of mouth referral, and to drive traffic to the (Corvel Press) web site.

The objective is to develop a post card template with clear and consistent brand imaging, but also with specific blank areas to be populated with multiple photos of respective properties which are to be uploaded with price and descriptive text - to be changed out with each new property being promoted for sale.

Bramble Arc Holdings, Inc. is an online and direct mail marketing service promoting available home buyer opportunities. The objective with each post card mailing is to capture lead contact information, and to promote the Bramble Arc Holdings brand. It is not important to promote any individual personality or person involved with Bramble Arc. Prospective buyer responses from the post card will be directed either to the dedicated web site, and/or to a dedicated customer service phone number. Both the URL and the dedicated phone # are to be highlighted on the post card.

In addition to specific properties for sale (photos and brief text on the front of card), an important function of the post card will be to promote various home buyer services (illustrated on the back of the card). Those various illustrated services are provided by an affiliated team of experienced professionals. The services are enumerated in the pencil concept draft attached with this application. Specifically those services are: Home Buyer Financing, Renovation Design Services, Project Cost Estimates, Rental Property Management, Professional CPA Consultation. Many of those services may be provided free of charge for qualified buyers.

Project Deadline Extended
Reason: I realize that the initial 3 day deadline is not realistic.

Target Market(s)

Real Estate Investors, Rehabbers, Landlords and First Time Home Buyers ...normally male, age 25-50 yr old.

Industry/Entity Type

Residential

Requirements
Must have
• 1. Ability to use basic template style for multiple property photo and text files.
2. A clear call to action and reference to dedicated web site URL and dedicated phone #.
3. Logo/branding to be consistent with web site and other promotional materials. i.e., business card, stationary, other template Bramble Arc post cards targeted to other niche markets.
Nice to have
• "Equity gain - opportunity - renovation" theme/background.

Clear distinct colors and photo images.

Trustworthy, reliable, professional look.
Should not have
• Casual/informal appearance.

Cluttered/overly detailed appearance.

```html
<!DOCTYPE html>
<html lang="en">
<head>
<meta charset="utf-8">
<title>Bramble Arc Holdings – Direct Mail Postcard</title>
<link rel="stylesheet" href="https://fonts.googleapis.com/css2?family=EB+Garamond:ital,wght@0,400;0,500;0,600;0,700;1,400&family=Roboto:ital,wght@1,700&display=swap">
<style>
  :root {
    --backdrop: #1c1c1c;
    --card: #ffffff;
    --green: #1f8a4f;
    --green-deep: #137a40;
    --green-light: #3ea266;
    --brown: #5b4326;
    --brown-dark: #3e2c16;
    --ink: #2f2f2f;
    --slot: #6f6f72;
    --slot-text: #545457;
    --tagline: #2c8a45;
  }
  * { box-sizing: border-box; margin: 0; padding: 0; }
  html, body { width: 1200px; height: 1200px; overflow: hidden; }
  body {
    background: var(--backdrop);
    font-family: "EB Garamond", Georgia, serif;
    position: relative;
  }
  .postcard {
    position: absolute;
    background: var(--card);
    box-shadow: 0 6px 18px rgba(0,0,0,.55);
  }

  /* ---------- Back side ---------- */
  .postcard--back { left: 420px; top: 26px; width: 726px; height: 558px; }
  .back-heading {
    position: absolute; left: 6px; top: 12px; width: 356px;
    text-align: center; color: var(--brown-dark);
  }
  .back-heading__lead { font-size: 25px; line-height: 30px; }
  .back-heading__brand { font-size: 33px; line-height: 40px; font-weight: 500; }
  .services {
    position: absolute; left: 6px; top: 90px; width: 356px; height: 284px;
    background: var(--green); color: #fff; list-style: none;
    padding: 12px 10px 0 12px;
  }
  .services__item { margin-bottom: 4px; }
  .services__title {
    display: flex; align-items: center; gap: 6px;
    font-size: 21px; font-weight: 600; line-height: 26px;
  }
  .services__title svg { flex: none; }
  .services__note {
    font-size: 18px; font-style: italic; line-height: 23px;
    padding-left: 26px; color: #e6f3ea;
  }
  .call-to-action {
    position: absolute; left: 6px; top: 379px; width: 356px; height: 85px;
    background: var(--brown); color: #fff; text-align: center; padding-top: 6px;
  }
  .call-to-action__line { font-size: 19px; line-height: 21px; }
  .call-to-action__phone { font-weight: 700; }
  .call-to-action__url { font-size: 27px; font-weight: 700; line-height: 34px; }
  .stamp-box {
    position: absolute; left: 550px; top: 10px; width: 166px; height: 166px;
    border: 1.5px solid #8c8c8c;
  }

  /* ---------- Front side ---------- */
  .postcard--front { left: 64px; top: 612px; width: 730px; height: 562px; }
  .photo-slot {
    position: absolute; width: 224px;
    background: linear-gradient(160deg, #7a7a7d, var(--slot));
    border: 2px solid #3d6a3a;
    display: flex; align-items: flex-end; justify-content: center;
    padding-bottom: 10px;
    font-family: Arial, Helvetica, sans-serif; font-weight: 700;
    font-size: 19px; color: var(--slot-text); letter-spacing: .5px;
  }
  .photo-slot--tl { left: 10px; top: 12px; height: 157px; border-top-left-radius: 18px; }
  .photo-slot--bl { left: 10px; top: 174px; height: 164px; }
  .photo-slot--tr { left: 496px; top: 12px; height: 157px; border-top-right-radius: 18px; }
  .photo-slot--br { left: 496px; top: 174px; height: 164px; }
  .offer-banner {
    position: absolute; left: 241px; top: 13px; width: 248px; height: 29px;
    background: var(--brown-dark); color: #fff; text-align: center;
    font-size: 23px; letter-spacing: 5px; line-height: 29px;
  }
  .offer-heading {
    position: absolute; left: 241px; top: 40px; width: 248px; text-align: center;
    font-size: 47px; line-height: 54px; color: var(--brown); letter-spacing: 1px;
  }
  .listing-panel {
    position: absolute; left: 241px; top: 94px; width: 248px; height: 244px;
    background: linear-gradient(160deg, var(--green-deep), var(--green-light));
    color: #fff; text-align: center; padding-top: 40px;
  }
  .listing-panel__headline { font-size: 28px; line-height: 36px; font-weight: 500; }
  .listing-panel__address { margin-top: 18px; font-size: 20px; line-height: 27px; }
  .divider {
    position: absolute; left: 10px; width: 710px; height: 2px; background: var(--brown);
  }
  .divider--top { top: 344px; }
  .divider--bottom { top: 528px; }
  .tagline {
    position: absolute; left: 18px; top: 396px;
    font-family: "Roboto", Arial, sans-serif; font-style: italic; font-weight: 700;
    font-size: 37px; color: var(--tagline); letter-spacing: -.3px;
  }
  .front-url {
    position: absolute; left: 74px; top: 448px;
    font-size: 28px; font-weight: 600; color: var(--ink);
  }
  .tree-art {
    position: absolute; left: 506px; top: 362px; width: 210px; height: 156px;
    background: radial-gradient(ellipse at 50% 40%, #2f9a55 0%, #48ad6a 55%, rgba(255,255,255,0) 72%);
  }
  .footer-band {
    position: absolute; left: 10px; top: 534px; width: 710px; height: 20px;
    background: linear-gradient(180deg, var(--brown), var(--brown-dark));
    border-radius: 0 0 12px 12px;
  }
</style>
</head>
<body>

<section class="postcard postcard--back" aria-label="Postcard back">
  <header class="back-heading">
    <p class="back-heading__lead">Get more with</p>
    <p class="back-heading__brand">BrambleArcHomes.com!</p>
  </header>

  <ul class="services">
    <li class="services__item">
      <p class="services__title"><svg width="18" height="18" viewBox="0 0 18 18"><rect x="1" y="1" width="15" height="15" fill="none" stroke="#fff" stroke-width="1.8"/><path d="M4 9l3.5 3.5L16 3" fill="none" stroke="#fff" stroke-width="2.2"/></svg>Afford the Dream</p>
      <p class="services__note">Specialized Financing Available</p>
    </li>
    <li class="services__item">
      <p class="services__title"><svg width="18" height="18" viewBox="0 0 18 18"><rect x="1" y="1" width="15" height="15" fill="none" stroke="#fff" stroke-width="1.8"/><path d="M4 9l3.5 3.5L16 3" fill="none" stroke="#fff" stroke-width="2.2"/></svg>Make it your own</p>
      <p class="services__note">Free Renovation Design</p>
    </li>
    <li class="services__item">
      <p class="services__title"><svg width="18" height="18" viewBox="0 0 18 18"><rect x="1" y="1" width="15" height="15" fill="none" stroke="#fff" stroke-width="1.8"/><path d="M4 9l3.5 3.5L16 3" fill="none" stroke="#fff" stroke-width="2.2"/></svg>Equity Gain Potential</p>
      <p class="services__note">Free renovation estimates</p>
    </li>
    <li class="services__item">
      <p class="services__title"><svg width="18" height="18" viewBox="0 0 18 18"><rect x="1" y="1" width="15" height="15" fill="none" stroke="#fff" stroke-width="1.8"/><path d="M4 9l3.5 3.5L16 3" fill="none" stroke="#fff" stroke-width="2.2"/></svg>Hassle Free Rental Income</p>
      <p class="services__note">Reliable Management Services</p>
    </li>
    <li class="services__item">
      <p class="services__title"><svg width="18" height="18" viewBox="0 0 18 18"><rect x="1" y="1" width="15" height="15" fill="none" stroke="#fff" stroke-width="1.8"/><path d="M4 9l3.5 3.5L16 3" fill="none" stroke="#fff" stroke-width="2.2"/></svg>Tax &amp; Accounting Guidance</p>
      <p class="services__note">Free 1 hr CPA Consultation</p>
    </li>
  </ul>

  <div class="call-to-action">
    <p class="call-to-action__line">Call to get more today! <span class="call-to-action__phone">317-555-0148</span></p>
    <p class="call-to-action__line">or visit us at</p>
    <p class="call-to-action__url">www.BrambleArcHomes.com</p>
  </div>

  <div class="stamp-box" aria-label="Postage area"></div>
</section>

<section class="postcard postcard--front" aria-label="Postcard front">
  <div class="photo-slot photo-slot--tl" role="img" aria-label="Property photo placeholder">TEMPLATE</div>
  <div class="photo-slot photo-slot--bl" role="img" aria-label="Property photo placeholder">TEMPLATE</div>
  <div class="photo-slot photo-slot--tr" role="img" aria-label="Property photo placeholder">TEMPLATE</div>
  <div class="photo-slot photo-slot--br" role="img" aria-label="Property photo placeholder">TEMPLATE</div>

  <p class="offer-banner">OPPORTUNITY</p>
  <h1 class="offer-heading">FOR SALE</h1>

  <div class="listing-panel">
    <p class="listing-panel__headline">This home is for<br>sale by owner</p>
    <p class="listing-panel__address">123 Your St., Your City<br>Your Country</p>
  </div>

  <div class="divider divider--top"></div>

  <p class="tagline">Own It! Restore It! Profit It!</p>
  <p class="front-url">www.BrambleArcHomes.com</p>
  <div class="tree-art" role="img" aria-label="Green tree silhouette illustration"></div>

  <div class="divider divider--bottom"></div>
  <div class="footer-band"></div>
</section>

</body>
</html>
```